Popup Banners - BrightCounsel - Legal Technology

- We need two banners (same style) designed with two different images and different text.

- The details of the printing requirements are attached, along with suggested images.

- The banners should share the same theme as our website www.brightcounsel.com.au

- The first banner would include our logo (attached), use the 'roads join' image (attached) in some way and text: New Opportunities - Where legal services and technology meet.

- The second banner would include our logo (attached), use the 'jigsaw' image (attached) in some way and use text: Legal Technology Strategy, Advice and Capability.

- Details on what are required from the Printer is attached also.

Target Market(s)

Legal Professionals

Industry/Entity Type

Information Technology

Font styles to use
Sans Serif

Requirements
Must have
• Our logo (attached), suggested text and the image mentioned for each.
Nice to have
• Professional and modern look
Should not have
• Cheap looking

```html
<!DOCTYPE html>
<html lang="en">
<head>
<meta charset="utf-8">
<title>BrightCounsel Popup Banners</title>
<link rel="stylesheet" href="https://fonts.googleapis.com/css2?family=Questrial&family=Roboto+Condensed:wght@400;500&display=swap">
<style>
  :root {
    --page: #ffffff;
    --frame: #3a3a3a;
    --brand-grey: #5a5350;
    --brand-blue: #5b9fd3;
    --ink-light: #ffffff;
    --jigsaw-deep: #1d4a74;
    --jigsaw-soft: #4f86b4;
    --roads-top: #4f8c4a;
    --roads-bottom: #3f7a2c;
  }
  * { margin: 0; padding: 0; box-sizing: border-box; }
  html, body { width: 1200px; height: 1200px; overflow: hidden; background: var(--page); }
  .canvas { position: relative; width: 1200px; height: 1200px; }

  .banner {
    position: absolute;
    top: 51px;
    width: 458px;
    height: 1102px;
    border: 1px solid var(--frame);
    overflow: hidden;
    background: var(--page);
  }
  .banner--jigsaw { left: 125px; }
  .banner--roads { left: 651px; }

  .banner__art { position: absolute; inset: 0; width: 100%; height: 100%; }

  .brand {
    position: absolute;
    top: 62px;
    left: 75px;
    display: flex;
    align-items: center;
    gap: 38px;
  }
  .brand__square { width: 34px; height: 34px; background: var(--brand-blue); }
  .brand__name {
    font-family: "Questrial", sans-serif;
    font-size: 31px;
    letter-spacing: 3.5px;
    color: var(--brand-grey);
    line-height: 1;
  }

  .tagline {
    position: absolute;
    text-align: right;
    font-family: "Roboto Condensed", sans-serif;
    font-size: 17px;
    letter-spacing: 2.6px;
    line-height: 26px;
    color: var(--ink-light);
    text-transform: uppercase;
    white-space: nowrap;
  }
  .banner--jigsaw .tagline { top: 444px; right: 30px; }
  .banner--roads .tagline { top: 224px; right: 104px; }

  .contact {
    position: absolute;
    left: 36px;
    top: 929px;
    font-family: "Roboto Condensed", sans-serif;
    color: var(--ink-light);
    text-transform: uppercase;
  }
  .contact__phone { font-size: 23px; letter-spacing: 0.3px; line-height: 1; }
  .contact__address { margin-top: 16px; font-size: 14px; letter-spacing: 0.3px; line-height: 1; }
</style>
</head>
<body>
<div class="canvas">

  <section class="banner banner--jigsaw">
    <svg class="banner__art" viewBox="0 0 343 827" preserveAspectRatio="none">
      <defs>
        <linearGradient id="jigsawTone" x1="0" y1="0" x2="1" y2="1">
          <stop offset="0" stop-color="var(--jigsaw-deep)"/>
          <stop offset="1" stop-color="var(--jigsaw-soft)"/>
        </linearGradient>
      </defs>
      <rect class="band" x="0" y="547" width="343" height="280" fill="var(--brand-blue)"/>
      <ellipse class="arc" cx="171" cy="397" rx="345" ry="273" fill="var(--brand-grey)"/>
      <ellipse class="photo" cx="171" cy="388" rx="340" ry="257" fill="url(#jigsawTone)"
               role="img" aria-label="Photo of a hand fitting a glowing jigsaw puzzle piece into place"/>
    </svg>
    <div class="brand"><span class="brand__square"></span><span class="brand__name">BrightCounsel</span></div>
    <p class="tagline">Legal technology strategy,<br>advice &amp; capability</p>
    <div class="contact">
      <p class="contact__phone">Contact us on 07 3100 4820</p>
      <p class="contact__address">Level 9, 120 Harbour Street Brisbane QLD, Australia</p>
    </div>
  </section>

  <section class="banner banner--roads">
    <svg class="banner__art" viewBox="0 0 343 827" preserveAspectRatio="none">
      <defs>
        <linearGradient id="roadsTone" x1="0" y1="0" x2="0" y2="1">
          <stop offset="0" stop-color="var(--roads-top)"/>
          <stop offset="1" stop-color="var(--roads-bottom)"/>
        </linearGradient>
      </defs>
      <rect class="band" x="0" y="547" width="343" height="280" fill="var(--brand-blue)"/>
      <ellipse class="arc" cx="171" cy="397" rx="345" ry="273" fill="var(--brand-grey)"/>
      <ellipse class="photo" cx="171" cy="388" rx="340" ry="257" fill="url(#roadsTone)"
               role="img" aria-label="Photo of two gravel roads joining on a grassy hill under a blue sky"/>
    </svg>
    <div class="brand"><span class="brand__square"></span><span class="brand__name">BrightCounsel</span></div>
    <p class="tagline">New opportunities - where<br>legal services and technology<br>come together</p>
    <div class="contact">
      <p class="contact__phone">Contact us on 07 3100 4820</p>
      <p class="contact__address">Level 9, 120 Harbour Street Brisbane QLD, Australia</p>
    </div>
  </section>

</div>
</body>
</html>
```